Business Card for IT company

I need a high tech looking business card using our logo. I prefer something clean and modern.

Target Market(s)

Buyers of IT hardware and software, IT Techies who are key influencers

Industry/Entity Type

Business

```html
<!DOCTYPE html>
<html lang="en">
<head>
<meta charset="utf-8">
<title>Norvale Consulting – Business Card</title>
<link rel="stylesheet" href="https://fonts.googleapis.com/css2?family=Ubuntu:wght@400;500&family=Raleway:wght@300;600&display=swap">
<style>
  :root {
    --backdrop: #2b2b2b;
    --card-dark: #3a3935;
    --card-dark-mark: #4f4e4a;
    --card-light: #ffffff;
    --ink: #333333;
    --accent: #7ab51d;
    --shadow: rgba(0,0,0,0.55);
  }
  * { margin: 0; padding: 0; box-sizing: border-box; }
  html, body { width: 1200px; height: 900px; overflow: hidden; }
  body {
    background: var(--backdrop);
    position: relative;
    font-family: "Ubuntu", sans-serif;
  }
  .card {
    position: absolute;
    top: 308px;
    width: 514px;
    height: 284px;
    box-shadow: 0 4px 10px var(--shadow);
  }
  .card--front { left: 73px; background: var(--card-dark); }
  .card--back  { left: 615px; background: var(--card-light); color: var(--ink); }

  /* front: large faint company name */
  .front-mark {
    position: absolute;
    left: 42px;
    top: 56px;
    width: 430px;
    color: var(--card-dark-mark);
    font-family: "Raleway", sans-serif;
    font-weight: 600;
    text-align: center;
  }
  .front-mark__name { font-size: 92px; line-height: 1; letter-spacing: -1px; }
  .front-mark__sub  { font-size: 34px; letter-spacing: 26px; margin-top: 14px; margin-right: -26px; font-weight: 600; }

  /* back: company name block */
  .brand {
    position: absolute;
    left: 44px;
    top: 108px;
    width: 200px;
    color: var(--ink);
    font-family: "Raleway", sans-serif;
    font-weight: 600;
    text-align: center;
  }
  .brand__name { font-size: 40px; line-height: 1; letter-spacing: -0.5px; }
  .brand__sub  { font-size: 12px; letter-spacing: 6.2px; margin-top: 10px; margin-right: -6px; }

  .divider {
    position: absolute;
    left: 272px;
    top: 54px;
    width: 2px;
    height: 177px;
    background: var(--accent);
  }

  .details {
    position: absolute;
    right: 43px;
    top: 56px;
    text-align: right;
    font-size: 13px;
    line-height: 17px;
  }
  .details__name { color: var(--accent); font-size: 20px; line-height: 24px; }
  .details__role { font-size: 15px; line-height: 20px; margin-bottom: 14px; }
  .contact-line { display: flex; justify-content: flex-end; align-items: center; gap: 6px; }
  .contact-line--no-icon { padding-right: 0; }
  .icon { width: 11px; height: 11px; fill: var(--accent); flex: none; }
  .address { margin-top: 14px; }
  .web-accent { color: var(--accent); }
</style>
</head>
<body>
  <section class="card card--front" aria-label="Card front">
    <div class="front-mark">
      <div class="front-mark__name">NORVALE</div>
      <div class="front-mark__sub">CONSULTING</div>
    </div>
  </section>

  <section class="card card--back" aria-label="Card back">
    <div class="brand">
      <div class="brand__name">NORVALE</div>
      <div class="brand__sub">CONSULTING</div>
    </div>

    <div class="divider"></div>

    <div class="details">
      <div class="details__name">Daniel Marrow</div>
      <div class="details__role">managing director</div>

      <div class="contact-line">888 888 88 88
        <svg class="icon" viewBox="0 0 12 12" aria-hidden="true"><path d="M3 0h6a1 1 0 0 1 1 1v10a1 1 0 0 1-1 1H3a1 1 0 0 1-1-1V1a1 1 0 0 1 1-1zm0.8 1.2v8.3h4.4V1.2zM6 10a0.6 0.6 0 1 0 0 1.2A0.6 0.6 0 0 0 6 10z" fill-rule="evenodd"/></svg>
      </div>
      <div class="contact-line">555 555 55 55
        <svg class="icon" viewBox="0 0 12 12" aria-hidden="true"><rect x="3" y="1" width="6" height="3"/><rect x="0.5" y="4.5" width="11" height="5" rx="1"/><rect x="3" y="8" width="6" height="3.5"/></svg>
      </div>
      <div class="contact-line">info@norvale.com
        <svg class="icon" viewBox="0 0 12 12" aria-hidden="true"><path d="M0.5 2.5h11v7h-11z"/><path d="M0.5 2.5L6 6.5l5.5-4" fill="none" stroke="#fff" stroke-width="1"/></svg>
      </div>

      <div class="address">
        <div>123 Fake Street</div>
        <div>Anytown, New York 12345</div>
        <div>www.<span class="web-accent">norvale</span>.com</div>
      </div>
    </div>
  </section>
</body>
</html>
```